Request for Business Card Design

Hi. My name is Marlena, I am looking for a new business card design for my company, Quillbrook Sensing Systems, LLC. I really like the design you did for Tavel Harvest and was hoping you could do something similar using our full logo and our mark. I am also open to any raised texture design using our mark. I have attached our full logo, which would need to be somewhere on the card, as well as the mark in both outline and full form, as well as our brand colors / guide. The card does not have to be white, as long as our logo and mark appear. I actually like darker colored business cards more, but am open to all options. If you are interested in working with me, please let me know. We would also take the business card design into letterhead design if you can do that.

```html
<!DOCTYPE html>
<html lang="en">
<head>
<meta charset="utf-8">
<title>Quillbrook Sensing Systems – Business Card</title>
<link href="https://fonts.googleapis.com/css2?family=Open+Sans:wght@400;600;700&display=swap" rel="stylesheet">
<style>
  :root {
    --backdrop: #3d3d3d;
    --card: #161616;
    --card-back: #121212;
    --accent: #1a9fd0;
    --text: #f2f2f2;
    --emboss: #2a2a2a;
  }
  * { box-sizing: border-box; margin: 0; padding: 0; }
  html, body {
    width: 1200px; height: 801px; overflow: hidden;
    background: var(--backdrop);
    font-family: "Open Sans", Arial, sans-serif;
  }
  .sheet {
    width: 1200px; height: 801px;
    display: flex; align-items: center; justify-content: center; gap: 40px;
  }
  .card {
    width: 540px; height: 309px;
    background: var(--card);
    border-bottom: 3px solid var(--accent);
    position: relative;
    box-shadow: 0 14px 30px rgba(0,0,0,.35);
  }
  .card--back { background: var(--card-back); }

  .brand { display: flex; align-items: center; gap: 12px; }
  .brand__dot { width: 34px; height: 34px; border-radius: 50%; background: var(--accent); flex: none; }
  .brand__name { font-weight: 700; font-size: 19px; letter-spacing: .5px; color: var(--text); line-height: 1.1; }

  .card--front .brand { position: absolute; left: 36px; bottom: 58px; width: 240px; }

  .divider { position: absolute; left: 292px; top: 34px; bottom: 34px; width: 1.5px; background: var(--accent); }

  .contact { position: absolute; left: 316px; top: 52px; right: 20px; color: var(--text); font-size: 12.5px; line-height: 1.45; }
  .contact__name { color: var(--accent); font-weight: 700; font-size: 17px; letter-spacing: .5px; text-transform: uppercase; }
  .contact__role { margin-bottom: 14px; }
  .contact__address { margin-bottom: 14px; }
  .contact__row { display: flex; align-items: center; gap: 8px; }
  .contact__row svg { width: 11px; height: 11px; flex: none; fill: var(--accent); }

  .card--back .brand { position: absolute; left: 50%; top: 50%; transform: translate(-50%, -50%); gap: 16px; }
  .card--back .brand__dot { width: 54px; height: 54px; background: var(--emboss); }
  .card--back .brand__name { font-size: 30px; color: var(--emboss); width: 300px; }
</style>
</head>
<body>
<main class="sheet">
  <section class="card card--front">
    <div class="brand">
      <span class="brand__dot"></span>
      <span class="brand__name">QUILLBROOK SENSING SYSTEMS</span>
    </div>
    <div class="divider"></div>
    <div class="contact">
      <div class="contact__name">Dorian Velasco</div>
      <div class="contact__role">President</div>
      <div class="contact__address">1820 Harbor Crest Dr<br>Seacliff CA 90210</div>
      <div class="contact__row">
        <svg viewBox="0 0 24 24" aria-hidden="true"><path d="M6.6 10.8a15.1 15.1 0 0 0 6.6 6.6l2.2-2.2c.3-.3.7-.4 1-.2 1.1.4 2.3.6 3.6.6.6 0 1 .4 1 1V20c0 .6-.4 1-1 1A17 17 0 0 1 3 4c0-.6.4-1 1-1h3.5c.6 0 1 .4 1 1 0 1.3.2 2.5.6 3.6.1.3 0 .7-.2 1z"/></svg>
        <span>555-014-7720</span>
      </div>
      <div class="contact__row">
        <svg viewBox="0 0 24 24" aria-hidden="true"><path d="M2 5h20v14H2zm2 2v.5l8 5 8-5V7zm0 2.8V17h16V9.8l-8 5z"/></svg>
        <span>d.velasco@quillbrook.com</span>
      </div>
      <div class="contact__row">
        <svg viewBox="0 0 24 24" aria-hidden="true"><path d="M12 2a10 10 0 1 0 0 20 10 10 0 0 0 0-20zm0 2c1 1.2 1.8 3 2.1 5H9.9C10.2 7 11 5.2 12 4zM4.3 14a8 8 0 0 1 0-4h3.6a17 17 0 0 0 0 4zm.8 2h3.1c.3 1.3.8 2.5 1.4 3.5A8 8 0 0 1 5.1 16zm3.1-8H5.1a8 8 0 0 1 4.5-3.5C9 5.5 8.5 6.7 8.2 8zM12 20c-1-1.2-1.8-3-2.1-5h4.2c-.3 2-1.1 3.8-2.1 5zm2.4-.5c.6-1 1.1-2.2 1.4-3.5h3.1a8 8 0 0 1-4.5 3.5zM16.1 14a17 17 0 0 0 0-4h3.6a8 8 0 0 1 0 4zm-.3-6c-.3-1.3-.8-2.5-1.4-3.5A8 8 0 0 1 18.9 8z"/></svg>
        <span>www.quillbrook.com</span>
      </div>
    </div>
  </section>

  <section class="card card--back">
    <div class="brand">
      <span class="brand__dot"></span>
      <span class="brand__name">QUILLBROOK SENSING SYSTEMS</span>
    </div>
  </section>
</main>
</body>
</html>
```